Business card design needed & Logo Design for Marketing

We need a business card design for a new beauty business. We offer Eyelash Extensions and beauty services, from our relaxing home based salon.

I would like the design to be modern and contemporary but with a twist of vintage thrown in. Our fave colour is Spearmint.

I also need a logo that can be embroidered onto uniforms.

Contact Information for Business Card

Willow Bloom Beauty
Eyelash Extensions and Beauty Services
18 Tindarra Crescent, Hollybank 4815
0418562971

```html
<!DOCTYPE html>
<html lang="en">
<head>
<meta charset="utf-8">
<title>Willow Bloom Beauty – Business Cards</title>
<link rel="stylesheet" href="https://fonts.googleapis.com/css2?family=Arimo:wght@400;700&display=swap">
<style>
  :root {
    --spearmint: #5fb08e;
    --spearmint-deep: #4e9d7c;
    --card-white: #ebebeb;
    --ink: #1b1b1b;
    --mist: #f4f4f4;
    --rule: #c9c9c9;
    --on-mint: #eef7f2;
  }
  * { margin: 0; padding: 0; box-sizing: border-box; }
  html, body {
    width: 1200px; height: 1000px; overflow: hidden;
    background: var(--mist);
    font-family: "Arimo", Arial, sans-serif;
    color: var(--ink);
  }
  .canvas {
    width: 1200px; height: 1000px;
    display: flex; flex-direction: column;
    align-items: center; justify-content: center; gap: 60px;
  }
  .card {
    width: 700px; height: 400px;
    border-radius: 4px;
    box-shadow: 0 10px 30px rgba(0,0,0,0.12);
    position: relative;
  }
  /* Front */
  .card-front {
    background: var(--spearmint);
    display: flex; flex-direction: column;
    align-items: center; justify-content: center; gap: 70px;
  }
  .brand-name {
    font-weight: 700; font-size: 50px; letter-spacing: 1px;
    text-transform: uppercase; text-align: center; line-height: 1.05;
  }
  .card-front .brand-name { color: var(--ink); }
  .services {
    color: var(--on-mint); font-size: 22px; letter-spacing: 0.5px;
    display: flex; align-items: center; gap: 16px;
  }
  .services .divider { width: 2px; height: 20px; background: var(--on-mint); }
  /* Back */
  .card-back {
    background: var(--card-white);
    display: flex; align-items: center;
    padding: 0 56px;
  }
  .card-back .brand-name {
    color: var(--ink); font-size: 36px; width: 250px; text-align: left;
  }
  .contact {
    margin-left: 40px; padding-left: 28px;
    border-left: 1px solid var(--rule);
    display: flex; flex-direction: column; gap: 10px;
  }
  .person { font-size: 34px; font-weight: 700; letter-spacing: -0.5px; }
  .person .surname { color: var(--spearmint); font-weight: 400; }
  .contact-line { font-size: 17px; display: flex; align-items: center; gap: 8px; }
  .contact-line svg { flex: none; }
  .email .local { color: var(--spearmint-deep); }
</style>
</head>
<body>
<main class="canvas">
  <section class="card card-front" aria-label="Business card front">
    <h1 class="brand-name">Willow Bloom<br>Beauty</h1>
    <p class="services">
      <span>Eyelash Extensions</span><span class="divider" aria-hidden="true"></span><span>Waxing Services</span>
    </p>
  </section>

  <section class="card card-back" aria-label="Business card back">
    <h2 class="brand-name">Willow Bloom Beauty</h2>
    <div class="contact">
      <p class="person">tessa<span class="surname">marlow</span></p>
      <p class="contact-line address">18 Tindarra Crescent, Hollybank 4815</p>
      <p class="contact-line phone">0418562971</p>
      <p class="contact-line email"><span><span class="local">tessa</span>@bloommail.com</span></p>
    </div>
  </section>
</main>
</body>
</html>
```